Velvet Jubilee Flyer

I need an 8.5x11 or 8.5x14 or 11x17 flyer for a benefit concert. Logo has already been designed; uploading several different versions, and you could choose which you want to use. For flyer design: something subtly musical (not a big fan of using musical symbols in the design, treble clefs, eighth notes, etc.) But something classy. I'm uploading unformatted copy, and two logos: one of the radio station that is helping to sponsor the event, and one for the organization the concert is benefitting. This is quick turnaround, so I promise to be very responsive with feedback. Thanks!

```html
<!DOCTYPE html>
<html lang="en">
<head>
<meta charset="utf-8">
<title>Velvet Jubilee Flyer</title>
<link rel="stylesheet" href="https://fonts.googleapis.com/css2?family=Raleway:wght@300;800&family=Source+Sans+3:wght@400;600;700&family=Arimo:wght@400&display=swap">
<style>
  :root {
    --ink: #111;
    --band-blue: #2f65a0;
    --heading-blue: #2e5e98;
    --bar-blue: #3b8fc7;
    --paper: #efefef;
    --grey-text: #4a4a4a;
    --white: #ffffff;
  }
  * { margin: 0; padding: 0; box-sizing: border-box; }
  html, body { width: 976px; height: 1200px; overflow: hidden; background: var(--paper); }
  .flyer { position: relative; width: 976px; height: 1200px; background: linear-gradient(180deg, #f6f6f6 0%, #eeeeee 100%); font-family: "Source Sans 3", sans-serif; color: var(--ink); }
  .hero-band { position: absolute; left: 0; top: 0; width: 976px; height: 620px; }
  .event-title { position: absolute; left: 0; right: 0; top: 80px; text-align: center; font-family: "Raleway", sans-serif; font-weight: 800; color: var(--white); line-height: 0.98; letter-spacing: 2px; }
  .event-title .line-1 { display: block; font-size: 62px; }
  .event-title .line-2 { display: block; font-size: 104px; }
  .event-title .line-3 { display: block; font-size: 80px; }
  .venue { position: absolute; left: 0; right: 0; top: 368px; text-align: center; font-family: "Raleway", sans-serif; font-weight: 300; color: var(--white); }
  .venue .church { display: block; font-size: 36px; }
  .venue .city { display: block; font-size: 34px; letter-spacing: 5px; margin-top: 2px; }
  .benefit { position: absolute; left: 0; right: 0; top: 566px; text-align: center; color: var(--heading-blue); font-weight: 700; line-height: 1.2; }
  .benefit .lead { display: block; font-size: 35px; }
  .benefit .cause { display: block; font-size: 36px; }
  .date-bar { position: absolute; left: 101px; top: 678px; width: 777px; height: 55px; background: var(--bar-blue); color: var(--white); font-family: "Arimo", sans-serif; font-size: 26px; display: flex; align-items: center; justify-content: center; }
  .featuring { position: absolute; left: 0; right: 0; top: 757px; text-align: center; font-size: 23px; }
  .including { position: absolute; left: 0; right: 0; top: 798px; text-align: center; font-family: "Arimo", sans-serif; font-size: 15px; color: var(--grey-text); }
  .lineup { position: absolute; left: 40px; right: 40px; top: 827px; text-align: center; font-family: "Arimo", sans-serif; font-size: 15.5px; line-height: 20.5px; color: var(--grey-text); }
  .admission { position: absolute; left: 0; right: 0; top: 957px; text-align: center; font-size: 22px; font-weight: 700; }
  .come-go { position: absolute; left: 0; right: 0; top: 993px; text-align: center; font-family: "Arimo", sans-serif; font-size: 15px; color: var(--grey-text); }
  .tickets { position: absolute; left: 284px; top: 1025px; width: 412px; height: 37px; background: var(--bar-blue); color: var(--white); font-family: "Arimo", sans-serif; font-size: 20px; display: flex; align-items: center; justify-content: center; }
  .schedule { position: absolute; left: 0; right: 0; top: 1076px; text-align: center; font-family: "Arimo", sans-serif; font-size: 15px; color: var(--grey-text); }
  .site { position: absolute; left: 0; right: 0; top: 1097px; text-align: center; font-size: 23px; font-weight: 700; color: var(--bar-blue); }
  .address { position: absolute; left: 0; right: 0; top: 1149px; text-align: center; font-family: "Arimo", sans-serif; font-size: 15.5px; color: var(--grey-text); }
  .partner { position: absolute; left: 52px; top: 1010px; width: 190px; text-align: center; }
  .partner .mark { display: block; width: 44px; height: 44px; margin: 0 auto 6px; background: var(--ink); }
  .partner .name { display: block; font-size: 17px; font-weight: 600; line-height: 1.1; color: var(--ink); }
  .sponsor { position: absolute; left: 736px; top: 1018px; width: 210px; text-align: center; }
  .sponsor .name { display: block; font-size: 21px; font-weight: 600; line-height: 1.2; color: var(--heading-blue); }
</style>
</head>
<body>
<main class="flyer">
  <svg class="hero-band" viewBox="0 0 976 620" aria-hidden="true">
    <polygon points="0,0 976,0 976,420 0,600" fill="#2f65a0"/>
    <polygon points="0,540 976,360 976,420 0,600" fill="#6c94c3" opacity="0.35" role="img" aria-label="Flowing musical staff sweeping across the lower edge of the band"/>
  </svg>

  <h1 class="event-title">
    <span class="line-1">MIDWINTER</span>
    <span class="line-2">VELVET</span>
    <span class="line-3">JUBILEE</span>
  </h1>

  <p class="venue">
    <span class="church">St. Aldric's Community Church</span>
    <span class="city">Albuquerque, New Mexico</span>
  </p>

  <h2 class="benefit">
    <span class="lead">A BENEFIT FOR</span>
    <span class="cause">DESERT HARBOR HEALTH OUTREACH</span>
  </h2>

  <div class="date-bar">Saturday, January 13, 2018 from12pm-8pm</div>

  <p class="featuring">Featuring some of New Mexico’s best musicians</p>
  <p class="including">INCLUDING:</p>
  <p class="lineup">Wind and Anvils, Jon Arbelle, The Oy! Calarino Clarinet Quartet, Joel Brennick, The Mesa Bassoon Band, The Rising Brass Quintet, Edwin Carraway, The Chew Toy Trio, Frederick Falmer, Frank Feldhaus, Kimberly Feldhaus, Fred Garland, Amy Greeve, Diana Holloway, Robert Lenz, Música Vieja del Río, The High Desert Chords, The Sandia Reed Winds, Quinta Choral Artists of the Southwest, Sol Cascada, Fred Stellan, Maxine Thérault, Kevin Vallant, Toby Vallant, Jacqueline Zeller-Ward</p>

  <p class="admission">Admission $25 ($10 for students)</p>
  <p class="come-go">Come and go as you like.</p>
  <div class="tickets">Tickets available at velvetjubilee.org</div>
  <p class="schedule">Full schedule available January 1.</p>
  <p class="site">www.velvetjubilee.org</p>
  <p class="address">St. Aldric's Community Church, 1418 Calder Avenue NE, Albuquerque</p>

  <div class="partner">
    <span class="mark"></span>
    <span class="name">Desert Harbor Health Outreach</span>
  </div>

  <div class="sponsor">
    <span class="name">Classical Public Radio 98.3 KVRL</span>
  </div>
</main>
</body>
</html>
```